Website-Design für die neue Handtaschenmarke Marvona
Zielgruppe
Frauen und auch Männer, die ästhetisch ausgearbeitete und gleichzeitig zweckmäßige Handtaschen und Accessoires suchen. Frauen, die Einzelstücke nach ihren Wünschen und Bedürfnissen angefertigt haben wollen.
Aufgabenstellung
Es soll die Startseite für eine Website mit einem kleinen angebundenen Online-Shop entstehen.
Es gibt keine bestehende Website, nur das Logo steht fest.
Das detailierte Briefing finden Sie als PDF Dokument in der Anlage.

```html
<!DOCTYPE html>
<html lang="de">
<head>
<meta charset="utf-8">
<title>Marvona – Kollektion</title>
<link href="https://fonts.googleapis.com/css2?family=Arimo:wght@400;700&family=Open+Sans:wght@300;400&display=swap" rel="stylesheet">
<style>
  :root {
    --brand-blue: #0e3f80;
    --ink: #2b2b2b;
    --muted: #555555;
    --page: #f2f2f2;
    --panel: #ffffff;
    --rule: #8a8a8a;
    --footer: #777777;
    --caption: rgba(255,255,255,0.78);
  }
  * { margin: 0; padding: 0; box-sizing: border-box; }
  html, body { width: 1066px; height: 1200px; overflow: hidden; }
  body {
    position: relative;
    background: var(--page);
    font-family: "Arimo", Helvetica, Arial, sans-serif;
    color: var(--ink);
  }
  a { color: inherit; text-decoration: none; }
  .abs { position: absolute; }

  /* Header */
  .brand { left: 44px; top: 30px; width: 110px; text-align: center; }
  .brand-mark { width: 46px; height: 46px; border-radius: 50%; background: var(--ink); margin: 0 auto 24px; }
  .brand-name { font-size: 18px; letter-spacing: 3px; color: var(--ink); }
  .account-links { left: 779px; top: 22px; font-size: 11px; color: var(--muted); }
  .lang { top: 21px; width: 17px; height: 12px; }
  .lang-de { left: 991px; }
  .lang-en { left: 1022px; }
  .main-nav { left: 279px; top: 114px; display: flex; gap: 0; font-size: 15px; color: var(--ink); }
  .main-nav a { position: absolute; white-space: nowrap; }
  .main-nav .active { color: var(--brand-blue); }

  /* Panel */
  .panel { left: 27px; top: 149px; width: 1016px; height: 944px; background: var(--panel); box-shadow: 0 0 6px rgba(0,0,0,0.18); }

  /* Sidebar */
  .sub-nav { left: 44px; top: 172px; width: 210px; list-style: none; font-size: 12px; text-transform: uppercase; }
  .sub-nav li { height: 42px; line-height: 24px; padding-left: 20px; color: var(--ink); }
  .sub-nav li.active { background: var(--brand-blue); color: #fff; height: 24px; margin-bottom: 18px; }

  .news { left: 44px; top: 576px; width: 215px; }
  .news-label { font-size: 14px; font-weight: 700; color: var(--brand-blue); }
  .news-date { font-family: "Open Sans", Arial, sans-serif; font-weight: 300; font-size: 25px; color: #444; margin-top: 6px; padding-bottom: 4px; border-bottom: 1px solid var(--rule); width: 210px; }
  .news-text { font-size: 12px; line-height: 20px; font-weight: 700; margin-top: 10px; margin-bottom: 14px; }
  .news-text .more { font-weight: 400; }
  .news-note { font-size: 12px; line-height: 20px; font-weight: 700; margin-top: 16px; }
  .newsletter { font-size: 13px; font-weight: 700; color: var(--brand-blue); margin-top: 14px; padding-bottom: 2px; border-bottom: 1px solid var(--rule); width: 210px; }
  .newsletter-note { font-size: 12px; font-weight: 700; margin-top: 12px; }
  .social { display: flex; gap: 15px; margin-top: 22px; }
  .social span { width: 28px; height: 28px; border-radius: 4px; background: #9a9a9a; display: block; }
  .social span:first-child { background: #3a5a98; }

  /* Main */
  .hero { left: 279px; top: 169px; width: 745px; height: 376px; border: 1px solid #bbb;
    background: radial-gradient(ellipse at 45% 50%, #3a4372 0%, #4d5687 40%, #8f96b6 70%, #e8e8ec 100%); }
  .headline { left: 279px; top: 570px; width: 760px; font-size: 37px; line-height: 46px; color: var(--brand-blue); font-weight: 400; }
  .teaser { top: 667px; width: 360px; }
  .teaser-left { left: 279px; }
  .teaser-right { left: 665px; }
  .teaser h3 { font-size: 12px; font-weight: 700; margin-bottom: 7px; }
  .teaser p.intro { font-size: 12px; line-height: 21px; color: var(--muted); }
  .teaser figure { position: relative; margin-top: 16px; width: 360px; height: 195px; border: 1px solid #aaa; overflow: hidden; }
  .teaser .photo { position: absolute; inset: 0; }
  .photo-blue { background: linear-gradient(160deg, #6f8fc4 0%, #3e5f9c 45%, #2b477f 100%); }
  .photo-orange { background: linear-gradient(170deg, #2a2a2a 0%, #3a3a3a 10%, #e0772f 16%, #d65a1c 60%, #b8461a 100%); }
  .teaser figcaption { position: absolute; left: 0; right: 0; bottom: 0; height: 51px; background: var(--caption); padding: 5px 0 0 24px; }
  .teaser figcaption strong { display: block; font-size: 19px; line-height: 22px; color: #111; }
  .teaser figcaption span { font-size: 13px; color: #222; }
  .teaser p.body { margin-top: 22px; font-size: 12px; line-height: 22px; color: var(--muted); }
  .teaser .more { color: var(--brand-blue); }

  /* Footer */
  .site-footer { left: 27px; top: 1112px; width: 1016px; height: 58px; background: var(--footer); color: #fff; font-size: 11px; text-align: center; line-height: 58px; }
</style>
</head>
<body>

<header>
  <div class="abs brand">
    <div class="brand-mark"></div>
    <div class="brand-name">MARVONA</div>
  </div>
  <div class="abs account-links">Mein Konto | Warenkorb | Zur Kasse</div>
  <svg class="abs lang lang-de" viewBox="0 0 17 12" aria-label="Deutsch">
    <rect width="17" height="4" fill="#111"/><rect y="4" width="17" height="4" fill="#d11"/><rect y="8" width="17" height="4" fill="#f5c400"/>
  </svg>
  <svg class="abs lang lang-en" viewBox="0 0 17 12" aria-label="English">
    <rect width="17" height="12" fill="#9aa"/><rect x="7" width="3" height="12" fill="#fff"/><rect y="4.5" width="17" height="3" fill="#fff"/>
  </svg>
  <nav class="abs main-nav">
    <a class="active" style="left:0">KOLLEKTION</a>
    <a style="left:122px">SHOP</a>
    <a style="left:190px">AUFTRAGSFERTIGUNG</a>
    <a style="left:386px">ÜBER MARVONA</a>
    <a style="left:530px">BLOG</a>
    <a style="left:601px">KONTAKT</a>
  </nav>
</header>

<div class="abs panel"></div>

<aside>
  <ul class="abs sub-nav">
    <li class="active">Kleine Handtaschen</li>
    <li>Grosse Handtaschen</li>
    <li>Lorem ipsum dolar</li>
    <li>Sitamet przert</li>
    <li>Zuitamet grterti</li>
  </ul>

  <section class="abs news">
    <div class="news-label">NEWS</div>
    <div class="news-date">05. August 2010</div>
    <p class="news-text">Lorem ipsum dolor sit amhkum, etur sadipscing elitr, sedumet my eirmod tempor invid klreilo <span class="more">(mehr...)</span></p>
    <div class="news-date">01. August 2010</div>
    <p class="news-text">Lorem ipsum dolor sit amhkum, etur sadipscing elitr, sedumet my eirmod tempor invid klreilo <span class="more">(mehr...)</span></p>
    <p class="news-note">Lorem ipsum dolor sit amh ilku, etn dolore magna aliq eratiom:</p>
    <div class="newsletter">NEWSLETTER</div>
    <p class="newsletter-note">Accusam eret justogte duresmi.</p>
    <div class="social"><span></span><span></span><span></span><span></span></div>
  </section>
</aside>

<main>
  <div class="abs hero" role="img" aria-label="Dunkelblaue Wildleder-Handtasche mit geflochtenem Riemen auf hellem Grund"></div>

  <h1 class="abs headline">Lorem ipsum domt amet, constetur Sadips amheft aklig weelitr condur akmetw.</h1>

  <article class="abs teaser teaser-left">
    <h3>Webet ultrices Proin non varius est. Cuabtur et hztum:</h3>
    <p class="intro">Ble diam, lacinia ut mattis in, fermeum eu tu. Alhlo wre jer Lenea isus quam, aliqueit torac, inter eratcm uzr loploi, weinean mass nulla ut ipsum malesuada meeu hertqwkilo.</p>
    <figure>
      <div class="photo photo-blue" role="img" aria-label="Hellblaue Stofftasche mit gerafften Falten"></div>
      <figcaption><strong>Jertzuter</strong><span>Bnjkhdeq thxjhki hrthx</span></figcaption>
    </figure>
    <p class="body">Lorem ipsum dolor sit amet, consetetur sadelitro ertnumy eirmod tempor invidunt ut labore et doloyam, sed loediam fertuzt uize voluptua tzuepö <span class="more">(mehr...)</span></p>
  </article>

  <article class="abs teaser teaser-right">
    <h3>Webet ultrices Proin non varius est. Cuabtur et hztum:</h3>
    <p class="intro">Ble diam, lacinia ut mattis in, fermeum eu tu. Alhlo wre jer Lenea isus quam, aliqueit torac, inter eratcm uzr loploi, weinean mass nulla ut ipsum malesuada meeu hertqwkilo.</p>
    <figure>
      <div class="photo photo-orange" role="img" aria-label="Orangefarbene Ledertasche mit Reißverschluss"></div>
      <figcaption><strong>Jertzuter</strong><span>Bnjkhdeq thxjhki hrthx</span></figcaption>
    </figure>
    <p class="body">Lorem ipsum dolor sit amet, consetetur sadelitro ertnumy eirmod tempor invidunt ut labore et doloyam, sed loediam fertuzt uize voluptua tzuepö (mehr...)</p>
  </article>
</main>

<footer class="abs site-footer">© Marvona 2010 | Impressum | AGB´s | Telefon: +49 4410 30125 | Fax: +49 4410 30126 | E-Mail: info(at)marvona-beispiel.de</footer>

</body>
</html>
```